The Willow Pawbright Dog Walking Service Website Design

I am looking for a professional website that demonstrates our love of dogs and their need for socialization and exercise. It should inspire client trust with their furry family member by emphasizing our professionalism & warm hearts. The website should have a consistent look that represents our brand. It should include a landing page with video images rather than still images. The website will include service descriptions with an image for each service, prices, awards won, frequently asked questions, reviews, blog, and links to a feed for our socials and the software that we use for booking etc. The website will highlight the different locations that we service & provide an "about us" section for each location.

```html
<!DOCTYPE html>
<html lang="en">
<head>
<meta charset="utf-8">
<title>The Willow Pawbright Dog Walking Service</title>
<link rel="stylesheet" href="https://fonts.googleapis.com/css2?family=Arimo:wght@400;700&display=swap">
<style>
  :root {
    --backdrop: #2e2e2e;
    --sky-left: #14c8fb;
    --sky-mid: #6fb4f2;
    --sky-right: #b9a6ee;
    --glow: #f59ad0;
    --ink: #141420;
    --button-face: #eef0fa;
    --button-edge: #a9a9c9;
    --button-text: #6a6ad8;
    --icon-line: #7d7db4;
    --cloud: #ffffff;
    --social-blue: #1877f2;
    --social-sky: #1da1f2;
    --social-red: #ff0000;
    --social-pink: #d6297a;
    --art-lilac: #b89ad6;
    --art-amber: #e0a060;
  }
  * { box-sizing: border-box; margin: 0; padding: 0; }
  html, body { width: 1200px; height: 1140px; overflow: hidden; }
  body {
    background: var(--backdrop);
    font-family: "Arimo", Arial, sans-serif;
    color: var(--ink);
    position: relative;
  }
  .landing {
    position: absolute;
    left: 0; top: 184px;
    width: 1200px; height: 760px;
    overflow: hidden;
    background: linear-gradient(90deg, var(--sky-left) 0%, var(--sky-mid) 50%, var(--sky-right) 100%);
  }
  .landing__glow {
    position: absolute;
    left: 250px; top: 40px;
    width: 600px; height: 560px;
    border-radius: 50%;
    background: radial-gradient(circle, var(--glow) 0%, rgba(245,154,208,0.55) 35%, rgba(245,154,208,0) 70%);
  }
  .brand-mark {
    position: absolute;
    left: 50px; top: 64px;
    display: flex; align-items: center; gap: 8px;
    font-size: 13px; font-weight: 700;
    color: var(--ink);
    width: 120px;
    line-height: 1.15;
  }
  .brand-mark__dot {
    flex: none;
    width: 22px; height: 22px;
    border-radius: 50%;
    background: var(--cloud);
  }
  .main-nav {
    position: absolute;
    right: 60px; top: 60px;
    display: flex; gap: 12px;
    font-size: 23px;
    list-style: none;
  }
  .main-nav li::after { content: " \25BE"; font-size: 20px; }
  .hero-title {
    position: absolute;
    left: 210px; top: 116px;
    font-size: 47px; font-weight: 700;
    line-height: 1.2;
  }
  .hero-art {
    position: absolute;
    left: 138px; top: 270px;
    width: 540px; height: 380px;
    border-radius: 46% 54% 40% 60% / 50% 45% 55% 50%;
    background: linear-gradient(135deg, var(--art-lilac) 0%, var(--art-lilac) 55%, var(--art-amber) 100%);
    opacity: 0.85;
  }
  .section-menu {
    position: absolute;
    left: 920px; top: 144px;
    list-style: none;
    display: flex; flex-direction: column; gap: 14px;
  }
  .section-menu li { position: relative; height: 70px; width: 160px; }
  .section-menu__pill {
    position: absolute;
    left: 26px; top: 10px;
    width: 130px; height: 50px;
    border-radius: 25px;
    background: var(--button-face);
    border: 1px solid var(--button-edge);
    display: flex; align-items: center; justify-content: center;
    padding-left: 36px;
    font-size: 20px;
    line-height: 1.05;
    text-align: center;
    color: var(--button-text);
  }
  .section-menu__icon {
    position: absolute;
    left: 0; top: 0;
    width: 70px; height: 70px;
  }
  .cloud-band { position: absolute; left: 0; bottom: 0; width: 1200px; height: 240px; }
  .socials {
    position: absolute;
    left: 922px; top: 650px;
    width: 240px;
  }
  .socials__label { font-size: 20px; color: var(--ink); margin-bottom: 12px; }
  .socials__list {
    list-style: none;
    display: grid;
    grid-template-columns: repeat(2, max-content);
    column-gap: 18px; row-gap: 8px;
    font-size: 14px; font-weight: 700;
  }
  .socials__list li { display: flex; align-items: center; gap: 6px; white-space: nowrap; }
  .socials__dot { width: 16px; height: 16px; border-radius: 50%; background: currentColor; }
  .socials__list li:nth-child(1) { color: var(--social-blue); }
  .socials__list li:nth-child(2) { color: var(--social-sky); }
  .socials__list li:nth-child(3) { color: var(--social-red); }
  .socials__list li:nth-child(4) { color: var(--social-pink); }
</style>
</head>
<body>
  <main class="landing">
    <div class="landing__glow"></div>

    <div class="brand-mark"><span class="brand-mark__dot"></span><span>The Willow Pawbright</span></div>

    <ul class="main-nav">
      <li>HOME</li>
      <li>CONTACT</li>
      <li>ABOUT US</li>
    </ul>

    <h1 class="hero-title">The Willow Pawbright<br>Dog Walking Service</h1>

    <div class="hero-art" role="img" aria-label="Illustration of a flying fairy in a lilac dress lifting a corgi among white stars"></div>

    <ul class="section-menu">
      <li>
        <span class="section-menu__pill">Service</span>
        <svg class="section-menu__icon" viewBox="0 0 70 70"><circle cx="35" cy="35" r="33" fill="var(--button-face)" stroke="var(--button-edge)" stroke-width="2"/><circle cx="35" cy="35" r="10" fill="none" stroke="var(--icon-line)" stroke-width="2.5"/><path d="M35 20v6M35 44v6M20 35h6M44 35h6M24 24l4 4M42 42l4 4M24 46l4-4M42 28l4-4" stroke="var(--icon-line)" stroke-width="2.5"/></svg>
      </li>
      <li>
        <span class="section-menu__pill">Prices</span>
        <svg class="section-menu__icon" viewBox="0 0 70 70"><circle cx="35" cy="35" r="33" fill="var(--button-face)" stroke="var(--button-edge)" stroke-width="2"/><rect x="25" y="21" width="20" height="28" fill="none" stroke="var(--icon-line)" stroke-width="2.5"/><text x="35" y="42" font-size="18" text-anchor="middle" fill="var(--icon-line)" font-family="Arimo, sans-serif">$</text></svg>
      </li>
      <li>
        <span class="section-menu__pill">awards<br>won</span>
        <svg class="section-menu__icon" viewBox="0 0 70 70"><circle cx="35" cy="35" r="33" fill="var(--button-face)" stroke="var(--button-edge)" stroke-width="2"/><circle cx="35" cy="35" r="12" fill="none" stroke="var(--icon-line)" stroke-width="2" stroke-dasharray="3 3"/></svg>
      </li>
      <li>
        <span class="section-menu__pill">reviews</span>
        <svg class="section-menu__icon" viewBox="0 0 70 70"><circle cx="35" cy="35" r="33" fill="var(--button-face)" stroke="var(--button-edge)" stroke-width="2"/><rect x="24" y="22" width="22" height="26" fill="none" stroke="var(--icon-line)" stroke-width="2"/><path d="M28 29h14M28 35h14M28 41h14" stroke="var(--icon-line)" stroke-width="2"/></svg>
      </li>
      <li>
        <span class="section-menu__pill">blog</span>
        <svg class="section-menu__icon" viewBox="0 0 70 70"><circle cx="35" cy="35" r="33" fill="var(--button-face)" stroke="var(--button-edge)" stroke-width="2"/><path d="M22 44h26M28 40l14-14" stroke="var(--icon-line)" stroke-width="2.5"/></svg>
      </li>
    </ul>

    <svg class="cloud-band" viewBox="0 0 1200 240" preserveAspectRatio="none">
      <path d="M0 170 C80 150 140 130 230 150 C320 172 380 190 470 170 C560 150 620 190 720 190 C800 190 830 130 900 120 C980 108 1080 90 1200 110 L1200 240 L0 240 Z" fill="var(--cloud)"/>
    </svg>

    <div class="socials">
      <p class="socials__label">Follows us on</p>
      <ul class="socials__list">
        <li><span class="socials__dot"></span>Wagly</li>
        <li><span class="socials__dot"></span>Tweetpaw</li>
        <li><span class="socials__dot"></span>Pupcast</li>
        <li><span class="socials__dot"></span>Snapbone</li>
      </ul>
    </div>
  </main>
</body>
</html>
```